New stationery design project

Until now, Brolin Technology was exclusively geared towards marketing the self-warming toasty-step insole. Corresponding designer material exists for this purpose, which is further used in this line of business. In the meantime, the business purpose has been expanded to include the following activities: "The company provides consulting services and takes on board mandates in the field of energy and information technology as well as personality-enhancing coaching." We now need a suitable stationery design (letterhead, business card) for this new business purpose. The design is intended to convey specialist knowledge and many years of experience

```html
<!DOCTYPE html>
<html lang="en">
<head>
<meta charset="utf-8">
<title>Brolin Technology – Business Card</title>
<link rel="stylesheet" href="https://fonts.googleapis.com/css2?family=Montserrat:wght@500;700&family=Lato:wght@400&display=swap">
<style>
  :root {
    --backdrop: #2b2b2b;
    --card-dark: #1f1f1f;
    --card-light: #ffffff;
    --ink-light: #ffffff;
    --ink-dark: #222222;
    --accent-red: #c8202a;
    --emboss: #3a3a3a;
  }
  * { margin: 0; padding: 0; box-sizing: border-box; }
  html, body { width: 1200px; height: 1015px; overflow: hidden; }
  body {
    background: var(--backdrop);
    position: relative;
    font-family: "Lato", sans-serif;
  }
  .card {
    position: absolute;
    left: 270px;
    width: 660px;
    height: 377px;
    background: var(--card-dark);
    overflow: hidden;
    box-shadow: 0 10px 28px rgba(0,0,0,0.45);
  }
  .card--back { top: 70px; }
  .card--front { top: 560px; }

  .back-brand {
    position: absolute;
    inset: 0;
    display: flex;
    align-items: center;
    justify-content: center;
    gap: 14px;
  }
  .back-brand__mark {
    width: 22px; height: 22px;
    background: var(--emboss);
  }
  .back-brand__name {
    font-family: "Montserrat", sans-serif;
    font-weight: 700;
    font-size: 40px;
    color: var(--emboss);
    letter-spacing: 0.5px;
  }

  .front-shape { position: absolute; inset: 0; }

  .front-brand {
    position: absolute;
    left: 330px;
    top: 150px;
    display: flex;
    align-items: center;
    gap: 10px;
  }
  .front-brand__mark {
    width: 16px; height: 16px;
    background: var(--accent-red);
  }
  .front-brand__name {
    font-family: "Montserrat", sans-serif;
    font-weight: 700;
    font-size: 27px;
    color: var(--ink-dark);
  }

  .holder {
    position: absolute;
    left: 60px;
    top: 62px;
    color: var(--ink-light);
  }
  .holder__name {
    font-family: "Montserrat", sans-serif;
    font-weight: 700;
    font-size: 24px;
    letter-spacing: 0.5px;
  }
  .holder__title {
    font-size: 15px;
    margin-top: 2px;
    letter-spacing: 0.3px;
  }

  .address {
    position: absolute;
    left: 60px;
    top: 200px;
    color: var(--ink-light);
    font-size: 15px;
    line-height: 1.3;
  }
  .contacts {
    position: absolute;
    left: 60px;
    top: 262px;
    list-style: none;
    color: var(--ink-light);
    font-size: 15px;
    line-height: 1.4;
  }
  .contacts li { display: flex; align-items: center; gap: 8px; }
  .contacts svg { width: 14px; height: 14px; fill: none; stroke: var(--ink-light); stroke-width: 1.6; }
</style>
</head>
<body>

  <section class="card card--back" aria-label="Business card back">
    <div class="back-brand">
      <span class="back-brand__mark"></span>
      <span class="back-brand__name">Brolin Technology</span>
    </div>
  </section>

  <section class="card card--front" aria-label="Business card front">
    <svg class="front-shape" viewBox="0 0 660 377" width="660" height="377" aria-hidden="true">
      <circle cx="520" cy="150" r="262" fill="var(--card-light)"/>
      <rect x="640" y="0" width="20" height="377" fill="var(--card-light)"/>
      <circle cx="528" cy="146" r="254" fill="none" stroke="var(--accent-red)" stroke-width="3"/>
    </svg>

    <div class="front-brand">
      <span class="front-brand__mark"></span>
      <span class="front-brand__name">Brolin Technology</span>
    </div>

    <div class="holder">
      <p class="holder__name">Marcus Hale</p>
      <p class="holder__title">Managing Director</p>
    </div>

    <p class="address">18, Harbor Lane<br>Country Name, 30817</p>

    <ul class="contacts">
      <li>
        <svg viewBox="0 0 16 16"><path d="M3 2h3l1.5 3.5-2 1.2a8 8 0 0 0 3.8 3.8l1.2-2L14 10v3a1 1 0 0 1-1 1A11 11 0 0 1 2 3a1 1 0 0 1 1-1z"/></svg>
        044-555 010 234
      </li>
      <li>
        <svg viewBox="0 0 16 16"><rect x="1.5" y="3.5" width="13" height="9"/><path d="M1.5 3.5 8 9l6.5-5.5"/></svg>
        info@brolintech.example
      </li>
      <li>
        <svg viewBox="0 0 16 16"><circle cx="8" cy="8" r="6.5"/><ellipse cx="8" cy="8" rx="3" ry="6.5"/><path d="M1.5 8h13"/></svg>
        www.brolintech.example
      </li>
    </ul>
  </section>

</body>
</html>
```